Emergency and Referral Vet Hospital promotional sticker design

We're looking at getting some stickers designed that we could give to clients to put on their cars for promotion and advertising. If they could also be suitable for a goodie bag for conference too that would be great. I like the look of water-colour backgrounds, we'll need to include our logo and probably our address (Unit 3/217 Marlowe Crescent Fairholt). We also have a hospital motto "... because they're family" if that could somehow be integrated, we only care for small animals (dogs, cats etc) but the design is very open to suggestion. Would love to see what you can create.

Industry/Entity Type

Veterinary

Colors
0054AA
0677BA
7BADD7
CADEEF
E8F1F8
0094D4
00A9DD
6FCCEA
C7EBF8
E9F6FB

Requirements
Nice to have
• Think beach vibes, blues maybe paw print shapes etc

```html
<!DOCTYPE html>
<html lang="en">
<head>
<meta charset="utf-8">
<title>Tidewell Vet Hospital – Sticker</title>
<link rel="stylesheet" href="https://fonts.googleapis.com/css2?family=Kaushan+Script&family=Nunito:wght@700;800&display=swap">
<style>
  :root {
    --page: #ffffff;
    --sticker: #f8f9fe;
    --wash-deep: #3cc6e6;
    --wash-mid: #6fccea;
    --wash-soft: #c7ebf8;
    --wash-lilac: #a9c2f3;
    --cross-line: rgba(255, 255, 255, 0.55);
    --motto: #123f5e;
    --ink: #0a0a0a;
  }
  * { margin: 0; padding: 0; box-sizing: border-box; }
  html, body {
    width: 1000px;
    height: 1200px;
    overflow: hidden;
    background: var(--page);
  }
  .sticker {
    position: absolute;
    left: 101px;
    top: 280px;
    width: 796px;
    height: 656px;
    background: var(--sticker);
    overflow: hidden;
  }
  .watercolour-wash {
    position: absolute;
    left: 48px;
    top: 8px;
    width: 742px;
    height: 630px;
    border-radius: 48% 52% 44% 56% / 46% 42% 58% 54%;
    background:
      radial-gradient(ellipse 38% 30% at 38% 48%, var(--wash-deep) 0%, rgba(60,198,230,0) 100%),
      radial-gradient(ellipse 30% 26% at 70% 40%, var(--wash-lilac) 0%, rgba(169,194,243,0) 100%),
      radial-gradient(ellipse 34% 24% at 40% 70%, var(--wash-mid) 0%, rgba(111,204,234,0) 100%),
      radial-gradient(ellipse 50% 50% at 50% 50%, var(--wash-soft) 30%, rgba(199,235,248,0) 100%);
  }
  .cross-frame {
    position: absolute;
    left: 0;
    top: 0;
    width: 796px;
    height: 656px;
  }
  .motto {
    position: absolute;
    left: 0;
    width: 100%;
    top: 268px;
    text-align: center;
    font-family: "Kaushan Script", cursive;
    font-size: 52px;
    line-height: 1;
    color: var(--motto);
  }
  .brand-name {
    position: absolute;
    left: 0;
    width: 100%;
    top: 490px;
    text-align: center;
    font-family: "Nunito", sans-serif;
    font-weight: 800;
    font-size: 46px;
    line-height: 1;
    color: var(--ink);
  }
  .address {
    position: absolute;
    left: 0;
    width: 100%;
    top: 552px;
    text-align: center;
    font-family: "Nunito", sans-serif;
    font-weight: 700;
    font-size: 16px;
    line-height: 22px;
    color: var(--ink);
  }
</style>
</head>
<body>
  <div class="sticker">
    <div class="watercolour-wash" role="img" aria-label="Soft blue and lilac watercolour wash scattered with white paw prints"></div>

    <svg class="cross-frame" viewBox="0 0 796 656" aria-hidden="true">
      <path d="M328 6 H470 Q494 6 494 30 V216 Q494 240 518 240 H720 Q744 240 744 264 V396 Q744 420 720 420 H518 Q494 420 494 444 V640 M304 640 V444 Q304 420 280 420 H74 Q50 420 50 396 V264 Q50 240 74 240 H280 Q304 240 304 216 V30 Q304 6 328 6"
            fill="none" stroke="var(--cross-line)" stroke-width="2"/>
    </svg>

    <p class="motto">… because they're family</p>
    <p class="brand-name">tidewell</p>
    <p class="address">Unit 3<br>217 Marlowe Crescent Fairholt</p>
  </div>
</body>
</html>
```